Brennick Holdings Business Cards

These are professional business cards that are for my family office.
Put fake emails and phone numbers as of now until I finalize those components. This family office controls my families investments, assets, and future. The cards should be professional.
..
.
.
.
I just uploaded another variation of a logo I would like to see as a business card to I am inbeteen which logo to use

Target Market(s)

business

Industry/Entity Type

business

Contact Information for Business Card

Professional, wealth related, finance related.

Requirements
Must have
• Logo

```html
<!DOCTYPE html>
<html lang="en">
<head>
<meta charset="UTF-8">
<title>Brennick Holdings Business Cards</title>
<link href="https://fonts.googleapis.com/css2?family=Montserrat:wght@400;500;700&display=swap" rel="stylesheet">
<style>
  :root {
    --backdrop: #3b3b3d;
    --card-white: #ffffff;
    --navy: #1b2135;
    --navy-text: #17305f;
    --ink: #1f1f24;
    --navy-relief: #2a3149;
    --silver-light: #e4e4e6;
    --silver-dark: #9a9a9e;
  }
  * { box-sizing: border-box; margin: 0; padding: 0; }
  html, body { width: 1200px; height: 1200px; overflow: hidden; }
  body {
    background: var(--backdrop);
    font-family: "Montserrat", sans-serif;
    display: flex;
    flex-direction: column;
    align-items: center;
    justify-content: center;
    gap: 56px;
  }
  .card {
    width: 900px;
    height: 514px;
    border-radius: 34px;
    position: relative;
    overflow: hidden;
  }

  /* Front */
  .card-front { background: var(--card-white); }
  .contact-block {
    position: absolute;
    left: 92px;
    top: 232px;
    color: var(--ink);
  }
  .person-name {
    font-weight: 700;
    font-size: 40px;
    color: var(--navy-text);
    letter-spacing: 0.5px;
    line-height: 1;
  }
  .person-title {
    font-weight: 400;
    font-size: 24px;
    margin-top: 6px;
    letter-spacing: 0.5px;
  }
  .contact-list { list-style: none; margin-top: 16px; }
  .contact-list li {
    display: flex;
    align-items: center;
    gap: 12px;
    font-size: 22px;
    line-height: 34px;
  }
  .contact-list svg { width: 22px; height: 22px; flex: none; fill: var(--navy-text); }
  .front-brand {
    position: absolute;
    left: 520px;
    top: 110px;
    width: 320px;
    display: flex;
    flex-direction: column;
    align-items: center;
    gap: 22px;
  }
  .brand-circle {
    width: 130px;
    height: 130px;
    border-radius: 50%;
    border: 3px solid var(--navy);
  }
  .brand-name {
    font-weight: 500;
    font-size: 28px;
    letter-spacing: 3px;
    text-transform: uppercase;
    color: var(--navy);
    white-space: nowrap;
  }
  .front-band {
    position: absolute;
    left: 0; right: 0; bottom: 0;
    height: 30px;
    display: flex;
  }
  .band-silver {
    width: 58%;
    background: linear-gradient(90deg, var(--silver-light), var(--silver-dark) 60%, var(--silver-light));
  }
  .band-gap { width: 12px; background: var(--card-white); }
  .band-navy { flex: 1; background: var(--navy); }

  /* Back */
  .card-back { background: var(--navy); }
  .relief-grid {
    position: absolute;
    inset: 40px 50px;
    display: grid;
    grid-template-columns: repeat(4, 1fr);
    grid-template-rows: repeat(3, 1fr);
    column-gap: 24px;
    align-items: center;
    justify-items: center;
  }
  .relief-mark {
    display: flex;
    flex-direction: column;
    align-items: center;
    gap: 10px;
  }
  .relief-mark .mark-circle {
    width: 62px; height: 62px;
    border-radius: 50%;
    border: 2px solid var(--navy-relief);
  }
  .relief-mark .mark-name {
    font-weight: 500;
    font-size: 12px;
    letter-spacing: 1px;
    text-transform: uppercase;
    color: var(--navy-relief);
    white-space: nowrap;
  }
  .relief-mark.is-featured .mark-circle { border-color: var(--card-white); }
  .relief-mark.is-featured .mark-name { color: var(--card-white); }
</style>
</head>
<body>

  <section class="card card-front">
    <div class="contact-block">
      <p class="person-name">FULL NAME</p>
      <p class="person-title">TITLE</p>
      <ul class="contact-list">
        <li>
          <svg viewBox="0 0 24 24" aria-hidden="true"><path d="M6.6 10.8a15.1 15.1 0 0 0 6.6 6.6l2.2-2.2c.3-.3.7-.4 1-.2 1.1.4 2.3.6 3.6.6.6 0 1 .4 1 1V20c0 .6-.4 1-1 1A17 17 0 0 1 3 4c0-.6.4-1 1-1h3.5c.6 0 1 .4 1 1 0 1.3.2 2.5.6 3.6.1.3 0 .7-.2 1z"/></svg>
          (000) 000 0000
        </li>
        <li>
          <svg viewBox="0 0 24 24" aria-hidden="true"><path d="M7 1h10a2 2 0 0 1 2 2v18a2 2 0 0 1-2 2H7a2 2 0 0 1-2-2V3a2 2 0 0 1 2-2zm0 3v14h10V4zm5 16a1 1 0 1 0 0 2 1 1 0 0 0 0-2z"/></svg>
          (000) 000 0000
        </li>
        <li>
          <svg viewBox="0 0 24 24" aria-hidden="true"><path d="M2 5h20v14H2zm2 2v.4l8 5.3 8-5.3V7zm0 2.8V17h16V9.8l-8 5.3z"/></svg>
          email@brennickmail.com
        </li>
        <li>
          <svg viewBox="0 0 24 24" aria-hidden="true"><path d="M12 2a10 10 0 1 0 0 20 10 10 0 0 0 0-20zm6.9 9h-3a15 15 0 0 0-1.3-5.6A8 8 0 0 1 18.9 11zM12 4c1 1.3 1.8 3.8 1.9 7h-3.8c.1-3.2.9-5.7 1.9-7zM9.4 5.4A15 15 0 0 0 8.1 11h-3a8 8 0 0 1 4.3-5.6zM5.1 13h3a15 15 0 0 0 1.3 5.6A8 8 0 0 1 5.1 13zm6.9 7c-1-1.3-1.8-3.8-1.9-7h3.8c-.1 3.2-.9 5.7-1.9 7zm2.6-1.4a15 15 0 0 0 1.3-5.6h3a8 8 0 0 1-4.3 5.6z"/></svg>
          www.brennickoffice.com
        </li>
      </ul>
    </div>

    <div class="front-brand">
      <div class="brand-circle"></div>
      <p class="brand-name">Brennick Holdings</p>
    </div>

    <div class="front-band">
      <div class="band-silver"></div>
      <div class="band-gap"></div>
      <div class="band-navy"></div>
    </div>
  </section>

  <section class="card card-back">
    <div class="relief-grid">
      <div class="relief-mark"><div class="mark-circle"></div><p class="mark-name">Brennick Holdings</p></div>
      <div class="relief-mark"><div class="mark-circle"></div><p class="mark-name">Brennick Holdings</p></div>
      <div class="relief-mark"><div class="mark-circle"></div><p class="mark-name">Brennick Holdings</p></div>
      <div class="relief-mark"><div class="mark-circle"></div><p class="mark-name">Brennick Holdings</p></div>
      <div class="relief-mark"><div class="mark-circle"></div><p class="mark-name">Brennick Holdings</p></div>
      <div class="relief-mark"><div class="mark-circle"></div><p class="mark-name">Brennick Holdings</p></div>
      <div class="relief-mark"><div class="mark-circle"></div><p class="mark-name">Brennick Holdings</p></div>
      <div class="relief-mark"><div class="mark-circle"></div><p class="mark-name">Brennick Holdings</p></div>
      <div class="relief-mark"><div class="mark-circle"></div><p class="mark-name">Brennick Holdings</p></div>
      <div class="relief-mark"><div class="mark-circle"></div><p class="mark-name">Brennick Holdings</p></div>
      <div class="relief-mark is-featured"><div class="mark-circle"></div><p class="mark-name">Brennick Holdings</p></div>
      <div class="relief-mark"><div class="mark-circle"></div><p class="mark-name">Brennick Holdings</p></div>
    </div>
  </section>

</body>
</html>
```